Modern labels for Tidlock products

We need a new design of our labels for the product “Tidlock” (https://www.tidlock.eu/#) . The reason why we want to change our labels is to get a modern and more advanced look of our product. We also want to create a unique product that is attractive for our customers, even if the product are used in hospitals and healthcare centers for collecting dangerous waste.

There is three sizes of labels (55x95, 90x95, 170x95 mm) for different boxes, but the label will contain similar information. There are certain requirements and factors from regulations/standards that you need to follow when you create the new layout. But it’s up to you to change the design. You can work with background, fonts, effects, colors, structure, pattern, new symbols, logotype etc. The label could be any color, but the container will stay yellow so they have to look good together.

Keywords: Elegant, modern, functional, attractive, exclusive

Target Market(s)

Hospitals and healthcare centers

Industry/Entity Type

Product

Font styles to use
Serif
Sans Serif

Colors

Designer to choose colors to be used in the design.

Requirements
Must have
• Requirements for the regulations ADR UN3291 and ISO 23907 (PDF).
• * Symbol for danger waste
• * Filling level
• * "Danger"
• * Symbol for no second use
• * Symbol for manufaturer
• * Referencenumber
• * Text "”Clinical waste, Unspecified, N.O.S.”"
• * Area for series, certification, size and useful capacity
• * Area for Illustrations.
• * Text “Autoclavable at 134 c”, “Do not force closure” and “Do not overfill”.
• * Text for certification ”UN 3291 1H2/Y0,3/S/YR/N/KVP4817B”
• Three different sizes (55x95, 90x95, 170x95).
• More info in PDF "3kravspecifikation"
Nice to have
• A modern, elegant, advanced look of our label.
Should not have
• The information must be clear and readable, not too decorative/handwriting fonts.

```html
<!DOCTYPE html>
<html lang="en">
<head>
<meta charset="utf-8">
<title>Tidlock clinical waste labels</title>
<link rel="stylesheet" href="https://fonts.googleapis.com/css2?family=Montserrat:wght@400;500;600;700;800;900&family=Saira+Condensed:wght@400;500;800&family=Saira+Extra+Condensed:wght@800;900&display=swap">
<style>
:root{
  --canvas:#ffec00;
  --label-yellow:#ffd500;
  --label-amber:#f7a600;
  --label-red:#e2231a;
  --label-plum:#6e3f78;
  --label-navy:#2b2f7a;
  --ink:#111111;
  --white:#ffffff;
  --frame:#8d8a86;
  --spec-label:#ffd400;
}
*{margin:0;padding:0;box-sizing:border-box}
html,body{width:1200px;height:848px;overflow:hidden;background:var(--canvas)}
body{position:relative;font-family:"Montserrat",sans-serif;color:var(--ink)}
.icon-defs{position:absolute;width:0;height:0}

.label{
  position:absolute;border:1.5px solid var(--frame);border-radius:12px;overflow:hidden;
  background:linear-gradient(100deg,var(--label-yellow) 0%,#ffcf00 42%,var(--label-amber) 60%,var(--label-red) 76%,#a0385e 88%,var(--label-plum) 100%);
}
.label-swoosh{position:absolute;inset:0;width:100%;height:100%}
.label > *:not(.label-swoosh){position:absolute}
.label--medium{left:275px;top:27px;width:363px;height:383px}
.label--narrow{left:740px;top:27px;width:220px;height:383px}
.label--wide{left:275px;top:435px;width:685px;height:383px}

.filling-level{left:0;right:0;height:2px;background:linear-gradient(90deg,var(--label-red) 0%,var(--label-red) 60%,#f0b000 100%)}
.filling-level span{position:absolute;top:-6px;padding:0 6px;background:var(--label-yellow);font-size:9px;letter-spacing:1.6px;font-weight:500;line-height:12px}

.heading{left:0;top:0;overflow:visible}
.heading .title{font-family:"Saira Extra Condensed","Arial Narrow",sans-serif;font-weight:900;fill:var(--ink)}
.heading .subtitle{font-family:"Saira Condensed","Arial Narrow",sans-serif;font-weight:400}

.hazard-diamond{display:block}
.un-block{text-align:center;font-weight:700}
.un-number{font-weight:800;letter-spacing:.5px;line-height:1}
.un-code{font-weight:700;line-height:1.2}
.un-danger{font-weight:800;letter-spacing:.4px;line-height:1.2}

.warnings{list-style:none}
.warnings li{display:flex;align-items:center;white-space:nowrap}
.warnings svg{flex:none}
.warnings .strong{font-weight:800}

.illustration-area{background:#fbfbfb;border-radius:8px;border:1px solid #f3e3a0}
.illustration-area .art{position:absolute;inset:6px;border-radius:4px;background:linear-gradient(160deg,#f4f4f4,#e9e9e9)}

.spec-table{border-radius:7px;background:linear-gradient(100deg,var(--label-red) 0%,#9c2a55 45%,var(--label-navy) 100%);color:var(--white);display:flex;flex-direction:column;justify-content:space-around}
.spec-row{display:flex;border-bottom:1px solid rgba(255,80,60,.8);font-weight:600}
.spec-row:last-child{border-bottom:none}
.spec-row dt{color:var(--spec-label);font-weight:500}

.fill-in{background:var(--white);border:1.5px solid var(--label-red);border-radius:7px;display:flex;flex-direction:column;justify-content:space-around}
.fill-in div{border-bottom:1px solid #9a9a9a;display:flex}
.fill-in div:last-child{border-bottom:none}

.maker-name{font-weight:800;line-height:1;display:flex;align-items:center;gap:3px}
.maker-name i{display:inline-block;background:var(--ink)}
.maker-info{font-weight:500;line-height:1.35}
.batch-code{font-size:7px;color:#c9a400;writing-mode:vertical-rl;transform:rotate(180deg);letter-spacing:.5px}

/* medium label */
.label--medium .filling-level{top:9px}
.label--medium .filling-level span{left:132px}
.label--medium .heading{width:363px;height:90px}
.label--medium .hazard-diamond{left:16px;top:64px;width:118px;height:118px}
.label--medium .un-block{left:0;width:150px;top:188px}
.label--medium .un-number{font-size:22px}
.label--medium .un-code{font-size:7px}
.label--medium .un-danger{font-size:12px;margin-top:4px}
.label--medium .warnings{left:10px;top:247px;font-size:9.5px}
.label--medium .warnings li{height:14.5px;gap:6px}
.label--medium .rule{left:10px;top:319px;width:136px;height:1px;background:#6b5b00}
.label--medium .maker-name{left:12px;top:329px;font-size:14px}
.label--medium .maker-info{left:12px;top:344px;font-size:5.5px}
.label--medium .factory{left:107px;top:354px}
.label--medium .illustration-area{left:152px;top:67px;width:200px;height:171px}
.label--medium .spec-table{left:152px;top:246px;width:200px;height:59px;padding:2px 8px;font-size:9.5px}
.label--medium .spec-row dt{width:86px}
.label--medium .fill-in{left:152px;top:313px;width:200px;height:59px;padding:2px 6px;font-size:9px}
.label--medium .fill-in span + span{margin-left:70px}
.label--medium .batch-code{left:354px;top:347px}

/* narrow label */
.label--narrow .filling-level{top:12px}
.label--narrow .filling-level span{left:66px;font-size:8px}
.label--narrow .heading{width:220px;height:70px}
.label--narrow .hazard-diamond{left:21px;top:61px;width:84px;height:84px}
.label--narrow .un-block{left:0;width:126px;top:150px}
.label--narrow .un-number{font-size:15px}
.label--narrow .un-code{font-size:5.3px}
.label--narrow .un-danger{font-size:8px;margin-top:3px}
.label--narrow .warnings{left:9px;top:192px;font-size:7.5px}
.label--narrow .warnings li{height:11.7px;gap:5px}
.label--narrow .illustration-area{left:126px;top:65px;width:88px;height:234px}
.label--narrow .spec-table{left:7px;top:245px;width:112px;height:52px;padding:1px 5px;font-size:6.6px}
.label--narrow .spec-row dt{margin-right:4px}
.label--narrow .fill-in{left:7px;top:304px;width:207px;height:48px;padding:1px 6px;font-size:7.5px}
.label--narrow .fill-in span + span{margin-left:66px}
.label--narrow .maker-name{left:8px;top:360px;font-size:11px}
.label--narrow .maker-info{left:72px;top:359px;font-size:5px}
.label--narrow .factory{left:180px;top:360px}
.label--narrow .batch-code{left:207px;top:358px;font-size:5px}

/* wide label */
.label--wide .filling-level{top:14px}
.label--wide .filling-level span{left:292px}
.label--wide .heading{width:685px;height:90px}
.label--wide .hazard-diamond{left:18px;top:94px;width:154px;height:154px}
.label--wide .un-block{left:0;width:190px;top:260px}
.label--wide .un-number{font-size:28px}
.label--wide .un-code{font-size:10px}
.label--wide .un-danger{font-size:15px;margin-top:7px}
.label--wide .warnings{left:189px;top:95px;font-size:14px}
.label--wide .warnings li{height:20px;gap:9px}
.label--wide .spec-table{left:187px;top:192px;width:200px;height:58px;padding:2px 8px;font-size:9.5px}
.label--wide .spec-row dt{width:86px}
.label--wide .fill-in{left:187px;top:263px;width:200px;height:60px;padding:2px 6px;font-size:9.5px}
.label--wide .fill-in span + span{margin-left:70px}
.label--wide .maker-name{left:187px;top:333px;font-size:14px}
.label--wide .maker-info{left:187px;top:348px;font-size:5.5px}
.label--wide .factory{left:250px;top:355px}
.label--wide .illustration-area{left:403px;top:97px;width:260px;height:229px}
.label--wide .batch-code{left:670px;top:295px;font-size:8px}
</style>
</head>
<body>

<svg class="icon-defs" aria-hidden="true">
  <defs>
    <symbol id="shield-tick" viewBox="0 0 12 12">
      <path d="M6 .5 11 2v4.2C11 9 8.6 10.9 6 11.7 3.4 10.9 1 9 1 6.2V2z" fill="#e2231a"/>
      <path d="M3.4 5.8 5.3 7.6 8.8 3.8" fill="none" stroke="#fff" stroke-width="1.6"/>
    </symbol>
    <symbol id="no-reuse" viewBox="0 0 14 14">
      <circle cx="7" cy="7" r="6" fill="none" stroke="#111" stroke-width="1.3"/>
      <text x="7" y="10.2" text-anchor="middle" font-family="Montserrat,sans-serif" font-weight="800" font-size="9" fill="#111">2</text>
      <path d="M2.8 11.2 11.2 2.8" stroke="#111" stroke-width="1.3"/>
    </symbol>
    <symbol id="factory" viewBox="0 0 16 14">
      <path d="M1 13V4h2v4l4-3v3l4-3v3l4-3v8z" fill="#111"/>
      <rect x="1" y="1" width="2" height="3" fill="#111"/>
    </symbol>
    <symbol id="hazard" viewBox="0 0 100 100">
      <rect x="14.6" y="14.6" width="70.8" height="70.8" transform="rotate(45 50 50)" fill="#fff"/>
      <rect x="18.6" y="18.6" width="62.8" height="62.8" transform="rotate(45 50 50)" fill="none" stroke="#111" stroke-width="2.2"/>
      <g fill="none" stroke="#111" stroke-width="3.2">
        <circle cx="50" cy="30" r="8"/>
        <circle cx="41" cy="45" r="8"/>
        <circle cx="59" cy="45" r="8"/>
        <circle cx="50" cy="40" r="11.5" stroke-width="2"/>
      </g>
      <circle cx="50" cy="40" r="3" fill="#111"/>
      <text x="50" y="80" text-anchor="middle" font-family="Montserrat,sans-serif" font-size="8" fill="#111">6</text>
    </symbol>
  </defs>
</svg>

<!-- 90 x 95 -->
<section class="label label--medium" aria-label="Label 90 by 95 mm">
  <svg class="label-swoosh" viewBox="0 0 100 100" preserveAspectRatio="none" aria-hidden="true">
    <path d="M0 70 C30 50 60 40 100 20 L100 35 C60 55 35 65 0 85Z" fill="#ffb400" opacity=".45"/>
    <path d="M55 100 C70 70 85 50 100 40 L100 100Z" fill="#c8262a" opacity=".35"/>
    <path d="M70 0 L100 0 100 25 C90 20 80 10 70 0Z" fill="#4b3a86" opacity=".5"/>
  </svg>
  <div class="filling-level"><span>FILLING LEVEL</span></div>
  <svg class="heading" viewBox="0 0 363 90" role="heading" aria-level="2">
    <text class="title" x="10" y="53" font-size="35" textLength="187" lengthAdjust="spacingAndGlyphs">CLINICAL WASTE</text>
    <text class="subtitle" x="212" y="53" font-size="19" fill="#fff" textLength="140" lengthAdjust="spacingAndGlyphs">UNSPECIFIED, N.O.S.</text>
  </svg>
  <svg class="hazard-diamond" viewBox="0 0 100 100" role="img" aria-label="Class 6 infectious substance hazard sign"><use href="#hazard"/></svg>
  <div class="un-block">
    <p class="un-number">UN3291</p>
    <p class="un-code">1H2/Y0,3/S/YR/N/KVP4817B</p>
    <p class="un-danger">DANGER</p>
  </div>
  <ul class="warnings">
    <li><svg width="10" height="10"><use href="#shield-tick"/></svg>Autoclavable at 134°C</li>
    <li><svg width="10" height="10"><use href="#shield-tick"/></svg>Do not force closure</li>
    <li><svg width="10" height="10"><use href="#shield-tick"/></svg>Do not overfill</li>
    <li class="strong"><svg width="10" height="10"><use href="#shield-tick"/></svg>NO SECOND USE <svg width="13" height="13"><use href="#no-reuse"/></svg></li>
  </ul>
  <div class="rule"></div>
  <p class="maker-name"><i style="width:8px;height:8px"></i>Tidlock</p>
  <p class="maker-info">Norrvik, Sweden<br>www.tidlock.eu<br>Ref: xxxxx-xx-xx-xx</p>
  <svg class="factory" width="14" height="12" aria-label="Manufacturer"><use href="#factory"/></svg>
  <div class="illustration-area"><div class="art" role="img" aria-label="Assembly and closure instruction drawings, steps 1 to 3"></div></div>
  <dl class="spec-table">
    <div class="spec-row"><dt>Series:</dt><dd>Aurel</dd></div>
    <div class="spec-row"><dt>Certification:</dt><dd>ISO 23907:2012</dd></div>
    <div class="spec-row"><dt>Size:</dt><dd>2,2 L</dd></div>
    <div class="spec-row"><dt>Useful capacity:</dt><dd>1,76 L</dd></div>
  </dl>
  <div class="fill-in">
    <div><span>Place / Clinic</span></div>
    <div><span>Department</span></div>
    <div><span>Sealed by</span><span>Date</span></div>
  </div>
  <p class="batch-code">2917-00</p>
</section>

<!-- 55 x 95 -->
<section class="label label--narrow" aria-label="Label 55 by 95 mm">
  <svg class="label-swoosh" viewBox="0 0 100 100" preserveAspectRatio="none" aria-hidden="true">
    <path d="M0 60 C30 45 65 30 100 15 L100 30 C65 45 30 60 0 75Z" fill="#ffb400" opacity=".45"/>
    <path d="M40 100 C60 75 80 60 100 50 L100 100Z" fill="#c8262a" opacity=".35"/>
    <path d="M60 0 L100 0 100 25 C85 15 75 8 60 0Z" fill="#4b3a86" opacity=".5"/>
  </svg>
  <div class="filling-level"><span>FILLING LEVEL</span></div>
  <svg class="heading" viewBox="0 0 220 70" role="heading" aria-level="2">
    <text class="title" x="8" y="45" font-size="28" textLength="142" lengthAdjust="spacingAndGlyphs">CLINICAL WASTE</text>
    <text class="subtitle" x="8" y="59" font-size="13" fill="#222" textLength="103" lengthAdjust="spacingAndGlyphs">UNSPECIFIED, N.O.S.</text>
  </svg>
  <svg class="hazard-diamond" viewBox="0 0 100 100" role="img" aria-label="Class 6 infectious substance hazard sign"><use href="#hazard"/></svg>
  <div class="un-block">
    <p class="un-number">UN3291</p>
    <p class="un-code">1H2/Y0,3/S/YR/N/KVP4817B</p>
    <p class="un-danger">DANGER</p>
  </div>
  <ul class="warnings">
    <li><svg width="8" height="8"><use href="#shield-tick"/></svg>Autoclavable at 134°C</li>
    <li><svg width="8" height="8"><use href="#shield-tick"/></svg>Do not force closure</li>
    <li><svg width="8" height="8"><use href="#shield-tick"/></svg>Do not overfill</li>
    <li class="strong"><svg width="8" height="8"><use href="#shield-tick"/></svg>NO SECOND USE <svg width="11" height="11"><use href="#no-reuse"/></svg></li>
  </ul>
  <div class="illustration-area"><div class="art" role="img" aria-label="Assembly and closure instruction drawings, steps 1 to 3"></div></div>
  <dl class="spec-table">
    <div class="spec-row"><dt>Series:</dt><dd>Aurel</dd></div>
    <div class="spec-row"><dt>Certification:</dt><dd>ISO 23907:2012</dd></div>
    <div class="spec-row"><dt>Size:</dt><dd>2,2 L</dd></div>
    <div class="spec-row"><dt>Useful capacity:</dt><dd>1,76 L</dd></div>
  </dl>
  <div class="fill-in">
    <div><span>Place / Clinic</span></div>
    <div><span>Department</span></div>
    <div><span>Sealed by</span><span>Date</span></div>
  </div>
  <p class="maker-name"><i style="width:7px;height:7px"></i>Tidlock</p>
  <p class="maker-info">Norrvik, Sweden &nbsp; www.tidlock.eu<br>Ref: xxxxx-xx-xx-xx</p>
  <svg class="factory" width="13" height="11" aria-label="Manufacturer"><use href="#factory"/></svg>
  <p class="batch-code">2917-00</p>
</section>

<!-- 170 x 95 -->
<section class="label label--wide" aria-label="Label 170 by 95 mm">
  <svg class="label-swoosh" viewBox="0 0 100 100" preserveAspectRatio="none" aria-hidden="true">
    <path d="M0 75 C30 55 60 35 100 15 L100 30 C60 50 30 70 0 92Z" fill="#ffb400" opacity=".45"/>
    <path d="M50 100 C65 75 80 62 100 55 L100 100Z" fill="#c8262a" opacity=".35"/>
    <path d="M72 0 L100 0 100 30 C88 22 80 12 72 0Z" fill="#4b3a86" opacity=".5"/>
  </svg>
  <div class="filling-level"><span>FILLING LEVEL</span></div>
  <svg class="heading" viewBox="0 0 685 90" role="heading" aria-level="2">
    <text class="title" x="15" y="75" font-size="55" textLength="300" lengthAdjust="spacingAndGlyphs">CLINICAL WASTE</text>
    <text class="subtitle" x="402" y="77" font-size="38" fill="#fff" textLength="263" lengthAdjust="spacingAndGlyphs">UNSPECIFIED, N.O.S.</text>
  </svg>
  <svg class="hazard-diamond" viewBox="0 0 100 100" role="img" aria-label="Class 6 infectious substance hazard sign"><use href="#hazard"/></svg>
  <div class="un-block">
    <p class="un-number">UN3291</p>
    <p class="un-code">1H2/Y0,3/S/YR/N/KVP4817B</p>
    <p class="un-danger">DANGER</p>
  </div>
  <ul class="warnings">
    <li><svg width="13" height="13"><use href="#shield-tick"/></svg>Autoclavable at 134°C</li>
    <li><svg width="13" height="13"><use href="#shield-tick"/></svg>Do not force closure</li>
    <li><svg width="13" height="13"><use href="#shield-tick"/></svg>Do not overfill</li>
    <li class="strong"><svg width="13" height="13"><use href="#shield-tick"/></svg>NO SECOND USE <svg width="18" height="18"><use href="#no-reuse"/></svg></li>
  </ul>
  <dl class="spec-table">
    <div class="spec-row"><dt>Series:</dt><dd>Aurel</dd></div>
    <div class="spec-row"><dt>Certification:</dt><dd>ISO 23907:2012</dd></div>
    <div class="spec-row"><dt>Size:</dt><dd>2,2 L</dd></div>
    <div class="spec-row"><dt>Useful capacity:</dt><dd>1,76 L</dd></div>
  </dl>
  <div class="fill-in">
    <div><span>Place / Clinic</span></div>
    <div><span>Department</span></div>
    <div><span>Sealed by</span><span>Date</span></div>
  </div>
  <p class="maker-name"><i style="width:8px;height:8px"></i>Tidlock</p>
  <p class="maker-info">Norrvik, Sweden<br>www.tidlock.eu<br>Ref: xxxxx-xx-xx-xx</p>
  <svg class="factory" width="14" height="12" aria-label="Manufacturer"><use href="#factory"/></svg>
  <div class="illustration-area"><div class="art" role="img" aria-label="Assembly and closure instruction drawings, steps 1 to 3"></div></div>
  <p class="batch-code">2917-00</p>
</section>

</body>
</html>
```